Postcard for NYC Education Class

The Larkfield Adult Learning Hub, an adult education center in New York City, seeks a postcard design to promote a classroom course called the Campus Pathway Seminar. The course walks adult learners through the college admissions, financial aid, and college enrollment processes.

You can learn more about the LALH and the LALH Campus Bridges Program at http://lalh.trvc.example.edu/ and http://lalhcampusbridges.org/.

The postcard should have text on two-sides.

SIDE #1
[LALH Logo]
Campus Pathway Seminar
A Classroom Course for LALH Students Interested in College-Going

Daytime Schedule: Wednesdays, 12:20 pm – 3:00 pm
Evening Schedule: Wednesdays, 5:00 pm – 6:15 pm

To learn more and enroll, visit the Campus Bridges Program in Room 1412 on your registration day. Apply now to guarantee a space!

SIDE #2
College Bound [in big Times New Roman Font in orange against a navy background…see http://lalh.trvc.example.edu/?page_id=1279&album=1&gallery=9]

[Sponsor Line: A sponsor line should appear in small italicized type on the front or back.]
The Larkfield Adult Learning Hub is administered by Tarrow Valley Community College/RSPU.

[Testimonial Quote: A testimonial quote should go on the front or on the back, preferably the back. ]
“Before taking the Campus Pathway Seminar, I wasn't sure how I would even start. The Workshop provided me with the information that I needed to go back to college.” -CPS Participant Spring 2013, Currently Attending Whitcombe Community College

Nice designs!  I like the designs by Studio by Marnie and Inkwell Forge themost.  

Target Market(s)

Adult education students, ages 18-40+.

The postcard will be distributed to prospective students in person. It will not be mailed and does not need to be designed for mailing.

Industry/Entity Type

Financial

Requirements
Must have
• The LALH is on its way towards having an official style guide. In the meantime, models that you can use are at http://lalhcampusbridges.files.examplepress.com/2013/06/cat-test-prep-workshop-postcard-final.pdf and at http://lalhcampusbridges.files.examplepress.com/2013/06/fee-waiver-1.pdf.

Also at https://pages.examplehost.net/site/plannedcampusefforts/home/campus-pathway-seminar/CPS%20Fall%202013%20Foamcore%20v1%20PDF.pdf?attredirects=0&d=1.

The colors are white, navy (pantone 533?), and yellow/orange.
Nice to have
• A scalloped border like in the postcard at http://lalhcampusbridges.files.examplepress.com/2013/06/cat-test-prep-workshop-postcard-final.pdf would be nice but is not necessary.

```html
<!DOCTYPE html>
<html lang="en">
<head>
<meta charset="utf-8">
<title>College Bound – Campus Pathway Seminar Postcard</title>
<link rel="stylesheet" href="https://fonts.googleapis.com/css2?family=Tinos:ital,wght@0,400;0,700;1,400&display=swap">
<style>
  :root {
    --navy: #1c2f5a;
    --yellow: #f3e614;
    --band-yellow: #f2dc12;
  }
  * { margin: 0; padding: 0; box-sizing: border-box; }
  html, body {
    width: 1200px;
    height: 924px;
    overflow: hidden;
    background: var(--navy);
  }
  .postcard {
    position: relative;
    width: 1200px;
    height: 924px;
    background: var(--navy);
    font-family: "Tinos", "Times New Roman", serif;
    color: var(--yellow);
  }
  .side-band {
    position: absolute;
    left: 0;
    top: 0;
    width: 117px;
    height: 924px;
    background: var(--band-yellow);
  }
  .side-rules {
    position: absolute;
    left: 117px;
    top: 0;
  }
  .headline {
    position: absolute;
    left: 117px;
    right: 0;
    top: 64px;
    text-align: center;
    font-weight: 700;
    font-size: 134px;
    line-height: 1;
    white-space: nowrap;
    padding-left: 28px;
  }
  .testimonial {
    position: absolute;
    left: 197px;
    top: 367px;
    font-size: 35px;
    line-height: 51px;
    white-space: nowrap;
  }
  .testimonial .attribution { display: block; }
  .sponsor-line {
    position: absolute;
    left: 168px;
    top: 813px;
    font-style: italic;
    font-size: 32px;
    line-height: 45px;
    white-space: nowrap;
  }
</style>
</head>
<body>
  <main class="postcard">
    <div class="side-band"></div>
    <svg class="side-rules" width="24" height="924" viewBox="0 0 24 924" aria-hidden="true">
      <rect x="6" y="0" width="2" height="924" fill="var(--band-yellow)"/>
      <rect x="12" y="0" width="2" height="924" fill="var(--band-yellow)"/>
      <rect x="18" y="0" width="2" height="924" fill="var(--band-yellow)"/>
    </svg>

    <h1 class="headline">College Bound</h1>

    <blockquote class="testimonial">
      <p>“Before taking the Campus Pathway Seminar,<br>
      I wasn't sure how I would even start.<br>
      The Workshop provided me with the information<br>
      that I needed to go back to college.”</p>
      <cite class="attribution" style="font-style: normal;">-CPS Participant Spring 2013,<br>
      Currently Attending Whitcombe Community College</cite>
    </blockquote>

    <p class="sponsor-line">The Larkfield Adult Learning Hub is administered by<br>
    Tarrow Valley Community College/RSPU</p>
  </main>
</body>
</html>
```